VornaDerm/The experts in permanent hairremoval

Our Brand is VornaDerm and we are specialized on permantent hair removal for the body for men and woman. VornaDerm is working as a Franchise chain.
The brand should be positioned as lifestyle brand but with a medical background. People should trust in us. We take care about their body. This need to be communicated 100%.
Our system is inexpensive but we don't want to show that we are cheap. So we want to communicate that permanent hair removal is a real lifestyle product but affordable.
We already created a logo that you can see the style and colour we prefer.

Target Market(s)

Europe beginning (especially german spoken markets), Middle East, Africa

Industry/Entity Type

Hair Removal

Number of Pages Required

5+ page

Font styles to use
Serif
Other font styles liked:
• Trajan Pro

Requirements
Nice to have
• We are very open for new ideas

```html
<!DOCTYPE html>
<html lang="en">
<head>
<meta charset="utf-8">
<title>VornaDerm – The Expert in Permanent Hair Removal</title>
<link rel="stylesheet" href="https://fonts.googleapis.com/css2?family=Open+Sans:wght@400;600;700&family=Lora:wght@400;700&display=swap">
<style>
:root{
  --blue:#2a9ad6;
  --blue-dark:#1d7fb8;
  --ink:#3a3a3a;
  --muted:#777;
  --band:#e4e4e4;
  --card:#f4f4f4;
  --footer:#2f3033;
  --footer-deep:#232427;
  --white:#fff;
  --hero-a:#d9d6d1;
  --hero-b:#b9b5ae;
}
*{box-sizing:border-box;margin:0;padding:0}
html,body{width:833px;height:1200px;overflow:hidden;background:var(--white)}
body{font-family:"Open Sans",Arial,sans-serif;color:var(--ink);font-size:9px;position:relative}
a{color:inherit;text-decoration:none}

/* header */
.site-header{position:absolute;top:0;left:0;width:833px;height:82px;background:var(--white)}
.brand{position:absolute;left:52px;top:18px;display:flex;align-items:center;gap:8px}
.brand-dot{width:30px;height:30px;border-radius:50%;background:var(--blue)}
.brand-name{font-family:"Lora",Georgia,serif;font-size:26px;font-weight:700;color:var(--blue)}
.account-links{position:absolute;right:52px;top:14px;display:flex;gap:26px;font-size:9px;color:var(--muted)}
.account-links span{display:flex;align-items:center;gap:5px}
.account-links i{width:10px;height:10px;border-radius:50%;background:var(--blue);display:inline-block}
.main-nav{position:absolute;right:52px;top:48px;display:flex;gap:15px;align-items:center;font-size:10.5px;font-weight:600;color:#444}
.main-nav svg{margin-left:4px}

/* hero */
.hero{position:absolute;top:82px;left:0;width:833px;height:422px;background:linear-gradient(90deg,var(--hero-b),var(--hero-a) 45%,#e9e7e3)}
.hero-photo{position:absolute;left:90px;top:0;width:300px;height:422px;background:linear-gradient(180deg,#8c7a6e,#4fa3a8 55%,#3f8790);opacity:.55}
.hero-copy{position:absolute;left:456px;top:134px}
.hero-copy h1{font-family:"Lora",Georgia,serif;font-size:36px;font-weight:400;color:#333}
.hero-copy p{font-family:"Lora",Georgia,serif;font-size:16px;color:#444;margin-top:6px}
.btn-book{display:inline-block;margin-top:18px;background:var(--blue);color:var(--white);font-size:12px;font-weight:600;padding:11px 20px;border-radius:3px;letter-spacing:.3px}
.slider-dots{position:absolute;left:396px;bottom:10px;display:flex;gap:5px}
.slider-dots i{width:6px;height:6px;border-radius:50%;background:#fff;opacity:.7}
.slider-dots i:first-child{opacity:1;background:var(--blue)}

/* features */
.features{position:absolute;top:504px;left:0;width:833px;height:225px;background:var(--band)}
.feature-list{position:absolute;left:55px;top:12px;display:flex;gap:18px}
.feature-card{width:167px;height:200px;background:var(--card);border:1px solid #d4d4d4;border-radius:4px;padding:8px}
.feature-card h3{font-family:"Lora",Georgia,serif;font-size:10.5px;text-align:center;margin-bottom:6px;color:#333}
.feature-img{height:70px;border-radius:3px}
.feature-card p{font-size:7.5px;line-height:1.5;color:var(--muted);margin-top:8px}
.read-more{display:block;text-align:right;font-size:8px;color:var(--blue);margin-top:12px;border-top:1px solid #ddd;padding-top:6px}

/* welcome + testimonials */
.about{position:absolute;top:742px;left:55px;width:440px}
.about h2,.testimonials h2{font-family:"Lora",Georgia,serif;font-size:22px;font-weight:400;color:#333;display:flex;align-items:center;gap:8px}
.about h2 i{width:22px;height:22px;border-radius:50%;background:var(--blue);display:inline-block}
.about p{font-size:8px;line-height:1.6;color:var(--muted);margin-top:14px}
.about ul{list-style:none;margin-top:10px}
.about li{font-size:8px;color:var(--muted);display:flex;align-items:center;gap:6px;margin-bottom:5px}
.testimonials{position:absolute;top:742px;left:520px;width:260px}
.testimonials h2 strong{color:var(--blue);font-weight:400}
.quote{position:relative;margin-top:16px;padding-left:26px;font-size:8px;line-height:1.6;color:var(--muted);width:175px}
.quote-mark{position:absolute;left:0;top:-6px;font-family:"Lora",Georgia,serif;font-size:34px;color:#ccc}
.quote-author{display:block;margin-top:10px;font-style:italic;color:#555}
.client-photo{position:absolute;right:0;top:60px;width:60px;height:60px;border-radius:50%;background:linear-gradient(135deg,#c9a58a,#8a6a58)}

/* footer */
.site-footer{position:absolute;top:962px;left:0;width:833px;height:238px}
.footer-curve{position:absolute;top:0;left:0}
.footer-cols{position:absolute;top:42px;left:55px;width:723px;display:flex;color:#cfd0d2}
.footer-cols h4{font-size:10px;font-weight:600;color:var(--white);margin-bottom:10px}
.quick-links{width:145px}
.quick-links li{list-style:none;font-size:7.5px;line-height:1.6;padding-left:8px;position:relative}
.quick-links li:before{content:"";position:absolute;left:0;top:5px;width:3px;height:3px;background:var(--blue)}
.inquiry{width:165px}
.field{height:12px;background:var(--white);border-radius:2px;margin-bottom:5px;width:120px;font-size:6.5px;color:#999;padding:1px 4px}
.field.tall{height:22px}
.btn-send{display:inline-block;background:var(--blue);color:var(--white);font-size:7px;padding:3px 10px;border-radius:2px}
.contact{width:255px}
.contact div{display:flex;gap:8px;align-items:flex-start;font-size:7.5px;line-height:1.5;margin-bottom:8px}
.contact b{flex:none;width:12px;height:12px;border-radius:2px;background:var(--blue)}
.footer-brand{flex:1;text-align:center;padding-top:26px}
.footer-brand .brand-name{font-size:20px}
.social{display:flex;gap:6px;justify-content:center;margin-top:14px}
.social i{width:16px;height:16px;border-radius:50%;background:var(--blue)}
.copyright{position:absolute;bottom:0;left:0;width:833px;height:22px;background:var(--footer-deep);color:#aaa;font-size:8px;text-align:center;line-height:22px}
</style>
</head>
<body>

<header class="site-header">
  <div class="brand"><span class="brand-dot"></span><span class="brand-name">VornaDerm</span></div>
  <div class="account-links">
    <span><i></i>Log In</span><span><i></i>Register</span><span><i></i>My Cart (0)</span>
  </div>
  <nav class="main-nav">
    <a>Home</a><a>About Us</a><a>Why Permanent Epilation</a><a>Prices</a><a>Jobs &amp; Careers</a><a>Franchise</a><a>Contact Us</a>
    <svg width="13" height="13" viewBox="0 0 13 13"><circle cx="5.5" cy="5.5" r="4" fill="none" stroke="#555" stroke-width="1.6"/><line x1="8.5" y1="8.5" x2="12" y2="12" stroke="#555" stroke-width="1.8"/></svg>
  </nav>
</header>

<section class="hero">
  <div class="hero-photo" role="img" aria-label="Woman in a flowing teal dress seated on a wooden chair"></div>
  <div class="hero-copy">
    <h1>VornaDerm</h1>
    <p>The Expert in Permanent Hair Removal</p>
    <a class="btn-book">BOOK AN APPOINTMENT</a>
  </div>
  <div class="slider-dots"><i></i><i></i><i></i><i></i></div>
</section>

<section class="features">
  <div class="feature-list">
    <article class="feature-card">
      <h3>Lorem Ipsum Dolor Sit</h3>
      <div class="feature-img" role="img" aria-label="Treatment of the lower legs" style="background:linear-gradient(135deg,#e8d6c8,#c6a58c)"></div>
      <p>Lorem ipsum dolor sit amet, in the adipiscing elit magna. Lorem ipsum dolor sit amet.</p>
      <a class="read-more">Read More »</a>
    </article>
    <article class="feature-card">
      <h3>Lorem Ipsum Dolor Sit</h3>
      <div class="feature-img" role="img" aria-label="Client relaxing during a back treatment" style="background:linear-gradient(135deg,#e6dcd2,#b9a393)"></div>
      <p>Lorem ipsum dolor sit amet, in the adipiscing elit magna. Lorem ipsum dolor sit amet.</p>
      <a class="read-more">Read More »</a>
    </article>
    <article class="feature-card">
      <h3>Lorem Ipsum Dolor Sit</h3>
      <div class="feature-img" role="img" aria-label="Facial skin care session" style="background:linear-gradient(135deg,#efe4da,#cbb19e)"></div>
      <p>Lorem ipsum dolor sit amet, in the adipiscing elit magna. Lorem ipsum dolor sit amet.</p>
      <a class="read-more">Read More »</a>
    </article>
    <article class="feature-card">
      <h3>Lorem Ipsum Dolor Sit</h3>
      <div class="feature-img" role="img" aria-label="Smiling client with smooth skin" style="background:linear-gradient(135deg,#e2c9b4,#9d7a63)"></div>
      <p>Lorem ipsum dolor sit amet, in the adipiscing elit magna. Lorem ipsum dolor sit amet.</p>
      <a class="read-more">Read More »</a>
    </article>
  </div>
</section>

<section class="about">
  <h2><i></i>Welcome to VornaDerm Treatments</h2>
  <p>Lorem ipsum dolor sit amet, consectetur adipiscing elit, sed diam nonummy nibh euismod tincidunt ut laoreet dolore magna aliquam erat volutpat. Ut wisi enim ad minim veniam, quis nostrud exerci tation ullamcorper suscipit lobortis nisl ut aliquip ex ea commodo consequat.</p>
  <ul>
    <li><svg width="9" height="9" viewBox="0 0 9 9"><path d="M1 4.5 3.5 7 8 1.5" fill="none" stroke="#2a9ad6" stroke-width="1.6"/></svg>Lorem ipsum dolor sit amet, consectetuer adipiscing elit</li>
    <li><svg width="9" height="9" viewBox="0 0 9 9"><path d="M1 4.5 3.5 7 8 1.5" fill="none" stroke="#2a9ad6" stroke-width="1.6"/></svg>Lorem ipsum dolor sit amet consectetuer</li>
    <li><svg width="9" height="9" viewBox="0 0 9 9"><path d="M1 4.5 3.5 7 8 1.5" fill="none" stroke="#2a9ad6" stroke-width="1.6"/></svg>Lorem ipsum dolor sit amet</li>
    <li><svg width="9" height="9" viewBox="0 0 9 9"><path d="M1 4.5 3.5 7 8 1.5" fill="none" stroke="#2a9ad6" stroke-width="1.6"/></svg>Lorem ipsum dolor sit amet, consectetuer adipiscing</li>
  </ul>
</section>

<section class="testimonials">
  <h2>Client <strong>Testimonials</strong></h2>
  <div class="quote">
    <span class="quote-mark">“</span>
    Lorem ipsum dolor sit amet, consectetuer adipiscing elit, sed diam nonummy nibh euismod tincidunt ut laoreet dolore magna aliquam erat.
    <span class="quote-author">- Lena Hartwig</span>
  </div>
  <div class="client-photo" role="img" aria-label="Portrait of a satisfied client"></div>
</section>

<footer class="site-footer">
  <svg class="footer-curve" width="833" height="238" viewBox="0 0 833 238">
    <path d="M0 20 Q416 -14 833 20 V238 H0Z" fill="#2a9ad6"/>
    <path d="M0 26 Q416 -6 833 26 V238 H0Z" fill="#2f3033"/>
  </svg>
  <div class="footer-cols">
    <div class="quick-links">
      <h4>Quick Links</h4>
      <ul><li>Home</li><li>About Us</li><li>Why Permanent Epilation</li><li>Prices</li><li>Jobs &amp; Careers</li><li>Franchise</li><li>Contact Us</li></ul>
    </div>
    <div class="inquiry">
      <h4>Quick Inquiry</h4>
      <div class="field">Name</div><div class="field">Email</div><div class="field tall">Message</div>
      <span class="btn-send">Send</span>
    </div>
    <div class="contact">
      <h4>Contact Details</h4>
      <div><b></b><span>12 Lindenweg, Suite 4<br>Clinic Quarter, Berlin 10115</span></div>
      <div><b></b><span>030-555-0192</span></div>
      <div><b></b><span>info@vornaderm-clinics.com</span></div>
    </div>
    <div class="footer-brand">
      <span class="brand-name">VornaDerm</span>
      <div class="social"><i></i><i></i><i></i></div>
    </div>
  </div>
  <div class="copyright">Copyright 2015 VornaDerm Treatments | All Rights Reserved</div>
</footer>

</body>
</html>
```